Brindle Oak MSP - Power Point Template Creation

I need someone to create a full slide deck template that is branded with logo and follows our color choices that can be used as a template to create presentations from.

```html
<!DOCTYPE html>
<html lang="en">
<head>
<meta charset="utf-8">
<title>Brindle Oak MSP – Slide Deck Template</title>
<link href="https://fonts.googleapis.com/css2?family=Montserrat:ital,wght@0,300;0,400;0,600;0,700;0,800;1,600&display=swap" rel="stylesheet">
<style>
:root{
  --bg:#d9d9d9;
  --ink:#231f20;
  --grey:#7a7a7a;
  --light:#eeeeee;
  --gold-1:#8c6a2c;
  --gold-2:#c9a45a;
  --gold-3:#f1dfa4;
  --gold-4:#a97c35;
  --gold:linear-gradient(120deg,var(--gold-1) 0%,var(--gold-2) 40%,var(--gold-3) 60%,var(--gold-4) 100%);
  --gold-v:linear-gradient(180deg,var(--gold-3) 0%,var(--gold-2) 40%,var(--gold-1) 100%);
  --photo:linear-gradient(135deg,#6e675f 0%,#b9b2a8 50%,#57514b 100%);
  --photo-dark:linear-gradient(135deg,#2a2826 0%,#4a4642 50%,#1b1a19 100%);
}
*{box-sizing:border-box;margin:0;padding:0}
html,body{width:1200px;height:2214px;overflow:hidden}
body{background:var(--bg);font-family:'Montserrat',sans-serif;color:var(--ink)}
.deck{position:absolute;left:54px;top:47px;display:grid;grid-template-columns:repeat(3,352px);grid-auto-rows:198px;column-gap:18.5px;row-gap:15px}
.slide{position:relative;overflow:hidden;background:#fff;box-shadow:0 2px 5px rgba(0,0,0,.25)}
.abs{position:absolute}
.num{position:absolute;right:8px;bottom:5px;font-size:4px;color:var(--ink)}
.photo{position:absolute;background:var(--photo)}
.photo.dark{background:var(--photo-dark)}
.gold{background:var(--gold)}
.gold-v{background:var(--gold-v)}
.dark-bg{background:var(--ink)}
.title{position:absolute;font-weight:700;font-size:11px;line-height:1.2}
.dash{position:absolute;width:14px;height:1.5px;background:var(--gold-2)}
.dash::after{content:"";position:absolute;left:16px;top:0;width:4px;height:1.5px;background:var(--ink)}
.txt{font-size:3.4px;line-height:1.45;color:var(--grey)}
.txt.w{color:#eee}
.h{font-size:5px;font-weight:700;color:var(--ink)}
.h.g{color:var(--gold-4)}
.h.w{color:#fff}
.brand{position:absolute;font-weight:600;font-size:7px;color:var(--ink);display:flex;align-items:center;gap:3px;white-space:nowrap}
.brand i{display:block;width:5px;height:5px;background:var(--gold-2)}
.sq{position:absolute;width:6px;height:6px;background:var(--gold-2)}
.big{position:absolute;font-size:20px;font-weight:400;line-height:1;white-space:nowrap}
.mk{position:absolute;font-size:12px;font-weight:700;color:var(--gold-4)}
.pres{position:absolute;font-size:8px;font-style:italic;font-weight:600}
.dots{position:absolute;display:flex;gap:3px}
.dots b{width:3px;height:3px;border-radius:50%;background:var(--ink)}
.dots b:nth-child(2){background:var(--gold-2)}
.web{position:absolute;font-size:6.5px;letter-spacing:3px;color:#fff;text-align:center}
.icon{position:absolute;border-radius:50%;background:var(--gold);display:flex;align-items:center;justify-content:center}
.icon::after{content:"";width:40%;height:40%;border:1px solid #fff;border-radius:50%}
.card{position:absolute;border:1px solid var(--ink);background:#fff;padding:4px}
.item{position:absolute}
</style>
</head>
<body>
<main class="deck">

<!-- 1 cover dark -->
<section class="slide" style="background:#161616">
  <div class="photo dark" style="inset:0" role="img" aria-label="Dark mountain landscape at dusk"></div>
  <div class="brand" style="left:112px;top:92px;font-size:13px;color:#fff"><i style="width:8px;height:8px"></i>Brindle Oak MSP</div>
</section>

<!-- 2 cover -->
<section class="slide">
  <div class="sq" style="left:8px;top:6px"></div>
  <div class="brand" style="left:20px;top:42px"><i></i>Brindle Oak MSP</div>
  <div class="big" style="left:20px;top:88px;font-size:19px">BUSINESS</div>
  <div class="mk" style="left:20px;top:111px">MARKETING</div>
  <div class="dash" style="left:20px;top:132px"></div>
  <div class="pres" style="left:20px;top:140px">Presentation</div>
  <div class="txt abs" style="left:20px;top:152px;width:95px">Lorem ipsum dolor sit amet, consectetuer adipiscing elit, sed diam nonum</div>
  <div class="dots" style="left:21px;top:178px"><b></b><b></b><b></b></div>
  <div class="gold abs" style="left:242px;top:0;width:110px;height:14px"></div>
  <div class="dark-bg abs" style="left:134px;top:150px;width:218px;height:48px"></div>
  <div class="abs" style="left:134px;top:8px;width:204px;height:176px;background:#fff"></div>
  <div class="photo" style="left:158px;top:24px;width:172px;height:152px" role="img" aria-label="Two businesswomen working on a laptop"></div>
</section>

<!-- 3 cover -->
<section class="slide">
  <div class="sq" style="left:8px;top:6px"></div>
  <div class="brand" style="left:20px;top:42px"><i></i>Brindle Oak MSP</div>
  <div class="big" style="left:20px;top:86px">BUSINESS</div>
  <div class="mk" style="left:20px;top:109px">MARKETING</div>
  <div class="dash" style="left:20px;top:130px"></div>
  <div class="pres" style="left:20px;top:137px">Presentation</div>
  <div class="txt abs" style="left:20px;top:149px;width:95px">Lorem ipsum dolor sit amet, consectetuer adipiscing elit, sed diam nonum</div>
  <div class="dots" style="left:21px;top:176px"><b></b><b></b><b></b></div>
  <div class="photo" style="left:148px;top:0;width:204px;height:160px" role="img" aria-label="Businesswomen reviewing work on a laptop"></div>
  <div class="gold abs" style="left:148px;top:160px;width:204px;height:38px"></div>
  <div class="web" style="left:148px;top:176px;width:204px">WWW.BRINDLEOAKMSP.COM</div>
</section>

<!-- 4 cover -->
<section class="slide">
  <div class="sq" style="left:8px;top:6px"></div>
  <div class="brand" style="left:20px;top:42px;font-size:6.5px"><i></i>Brindle Oak MSP</div>
  <div class="big" style="left:20px;top:94px">BUSINESS</div>
  <div class="mk" style="left:20px;top:116px">MARKETING</div>
  <div class="dash" style="left:20px;top:138px"></div>
  <div class="pres" style="left:20px;top:144px">Presentation</div>
  <div class="txt abs" style="left:20px;top:156px;width:95px">Lorem ipsum dolor sit amet, consectetuer adipiscing elit, sed diam nonum</div>
  <div class="dots" style="left:21px;top:180px"><b></b><b></b><b></b></div>
  <div class="photo" style="left:148px;top:0;width:204px;height:162px" role="img" aria-label="Two businessmen discussing at a laptop"></div>
  <div class="gold abs" style="left:148px;top:162px;width:204px;height:36px"></div>
  <div class="web" style="left:148px;top:177px;width:204px">WWW.BRINDLEOAKMSP.COM</div>
</section>

<!-- 5 agenda -->
<section class="slide">
  <div class="photo" style="left:48px;top:0;width:170px;height:198px" role="img" aria-label="Team meeting in a bright office"></div>
  <div class="gold-v abs" style="left:30px;top:30px;width:37px;height:138px"></div>
  <div class="abs" style="top:58px;transform:rotate(90deg);transform-origin:left top;left:60px;font-size:16px;font-weight:800;color:#fff">Agenda</div>
  <div class="gold-v abs" style="right:0;top:30px;width:4px;height:138px"></div>
  <div class="item" style="left:188px;top:42px;width:140px"><div class="h">1. Lorem Ipsum</div><div class="txt" style="margin:2px 0 0 8px">Lorem ipsum dolor sit amet, consectetuer adipiscing elit, sed diam nonummy nibh euismod tincid</div></div>
  <div class="item" style="left:188px;top:74px;width:140px"><div class="h">2. Lorem Ipsum</div><div class="txt" style="margin:2px 0 0 8px">Lorem ipsum dolor sit amet, consectetuer adipiscing elit, sed diam nonummy nibh euismod tincid</div></div>
  <div class="item" style="left:188px;top:106px;width:140px"><div class="h">3. Lorem Ipsum</div><div class="txt" style="margin:2px 0 0 8px">Lorem ipsum dolor sit amet, consectetuer adipiscing elit, sed diam nonummy nibh euismod tincid</div></div>
  <div class="item" style="left:188px;top:138px;width:140px"><div class="h">4. Lorem Ipsum</div><div class="txt" style="margin:2px 0 0 8px">Lorem ipsum dolor sit amet, consectetuer adipiscing elit, sed diam nonummy nibh euismod tincid</div></div>
  <div class="num">2</div>
</section>

<!-- 6 -->
<section class="slide">
  <div class="abs" style="left:0;top:60px;width:5px;height:100px;background:var(--gold-v)"></div>
  <div class="title" style="left:19px;top:60px;font-size:21px;font-weight:800;line-height:1.05">Text<br><span style="color:var(--gold-4)">Added</span><br>Here</div>
  <div class="photo" style="left:112px;top:32px;width:240px;height:97px" role="img" aria-label="Charts and reports on a desk"></div>
  <div class="card" style="left:152px;top:95px;width:72px;height:88px;border:none;box-shadow:0 1px 3px rgba(0,0,0,.3);padding:0">
    <div class="dark-bg" style="height:16px;color:#fff;font-size:7px;font-weight:700;padding:4px 0 0 6px">Text Here</div>
    <div class="txt" style="padding:4px 6px">Lorem ipsum dolor sit amet, consectetuer adipiscing elit, sed diam nonummy nibh euismod tincidunt ut laoreet dolore magna aliquam erat volutpat. Ut wisi enim ad minim veniam, quis nostrud exerci tation.</div>
  </div>
  <div class="card" style="left:240px;top:95px;width:72px;height:88px;border:none;box-shadow:0 1px 3px rgba(0,0,0,.3);padding:0">
    <div class="dark-bg" style="height:16px;color:#fff;font-size:7px;font-weight:700;padding:4px 0 0 6px">Text Here</div>
    <div class="txt" style="padding:4px 6px">Lorem ipsum dolor sit amet, consectetuer adipiscing elit, sed diam nonummy nibh euismod tincidunt ut laoreet dolore magna aliquam erat volutpat. Ut wisi enim ad minim veniam, quis nostrud exerci tation.</div>
  </div>
  <div class="num">3</div>
</section>

<!-- 7 -->
<section class="slide">
  <div class="gold-v abs" style="left:0;top:0;width:9px;height:198px"></div>
  <div class="gold abs" style="left:275px;top:0;width:77px;height:74px"></div>
  <div class="gold abs" style="left:0;top:186px;width:245px;height:12px"></div>
  <div class="title" style="left:33px;top:40px;font-size:11px;font-weight:800;letter-spacing:.5px">Lorem Ipsum<br>Dolor Sit<br>Ametkeeper.</div>
  <div class="dash" style="left:33px;top:84px"></div>
  <div class="txt abs" style="left:33px;top:94px;width:110px">Lorem ipsum dolor sit amet, consectetuer adipiscing elit, sed diam nonummy nibh euismod tincidunt ut laoreet dolore magna aliquam erat volutpat. Ut wisi it feb odo consequat. Duis autem lore te feugait nulla facilisi.<br><br>Lorem ipsum dolor sit amet, cons ectetuer adipiscing elit, sed diam nonh ad minim veniam, quis nostrud exerci tation ullamcorper</div>
  <div class="photo dark" style="left:170px;top:36px;width:162px;height:102px;background:linear-gradient(135deg,#3a2418,#7a4a2a,#24160f)" role="img" aria-label="Person lying in autumn leaves covering their eyes"></div>
  <div class="num">4</div>
</section>

<!-- 8 part one -->
<section class="slide">
  <div class="gold-v abs" style="left:0;top:0;width:9px;height:198px"></div>
  <div class="title" style="left:32px;top:70px;font-size:15px">Part One</div>
  <div class="txt abs" style="left:32px;top:90px;width:110px">Lorem ipsum dolor sit amet, laoreet dolore magna aliquam erat volutpat. Ut wisi it lob odo consequat. Duis autem lore te feugait nulla facilisi.<br><br>Lorem ipsum dolor sit amet, cons ectetuer adipiscing elit, sed diam nonh ad minim veniam, quis nostrud exerci tation ullamcorper</div>
  <div class="photo dark" style="left:191px;top:18px;width:140px;height:162px;background:linear-gradient(160deg,#1c2226,#5b4a2e,#141719)" role="img" aria-label="Hands holding a glowing light bulb"></div>
  <div class="gold abs" style="left:156px;top:60px;width:78px;height:76px;display:flex;align-items:center;justify-content:center;color:#fff;font-size:44px;font-weight:700">01</div>
  <div class="num">5</div>
</section>

<!-- 9 stats -->
<section class="slide">
  <div class="gold-v abs" style="left:0;top:0;width:5px;height:198px"></div>
  <div class="title" style="left:19px;top:14px;font-size:13px;font-weight:800;line-height:1.15">Lorem<br>Dolor Sit<br>Consectetuer</div>
  <div class="txt abs" style="left:19px;top:82px;width:150px">Lorem ipsum dolor sit amet, consectetuer adipiscing elit, sed diam nonummy nibh euismod tincidunt ut laoreet dolore magna aliquam erat volutpat Ut wisi enim ad minim veniam, quis nostrud exerci tation ullamcorper suscipit</div>
  <div class="abs" style="left:210px;top:40px"><div style="font-size:10px;font-weight:700;color:var(--gold-4)">768K</div><div class="h">Lorem Ipsum</div><div class="txt" style="width:50px">Lorem ipsum dolor sit amet, consectetuer elit.</div></div>
  <div class="abs" style="left:282px;top:40px"><div style="font-size:10px;font-weight:700;color:var(--gold-4)">423K</div><div class="h">Lorem Ipsum</div><div class="txt" style="width:50px">Lorem ipsum dolor sit amet, consectetuer elit.</div></div>
  <div class="gold abs" style="left:200px;top:106px;width:152px;height:22px;color:#fff;font-size:10px;font-weight:700;padding:5px 0 0 10px">Text Added Here</div>
  <div class="gold-v abs" style="left:78px;top:130px;width:5px;height:68px"></div>
  <div class="photo" style="left:86px;top:130px;width:244px;height:68px" role="img" aria-label="Presenter leading a team workshop"></div>
  <div class="num" style="color:#fff">6</div>
</section>

<!-- 10 bar chart -->
<section class="slide">
  <div class="title" style="left:18px;top:14px">Text<br>Added Hare</div>
  <div class="dash" style="left:18px;top:45px"></div>
  <div class="dark-bg abs" style="left:0;top:59px;width:113px;height:116px"></div>
  <div class="abs" style="left:18px;top:70px;width:90px">
    <div style="display:flex;gap:4px;margin-bottom:11px"><div class="gold" style="width:12px;height:12px;color:#fff;font-size:8px;font-weight:700;text-align:center;line-height:12px">1.</div><div><div class="h" style="color:var(--gold-2)">Lorem ipsum</div><div class="txt w">Lorem ipsum dolor sit amet, consectetuer adipiscing elit, sed diam nonummy nibh euismod tincid</div></div></div>
    <div style="display:flex;gap:4px;margin-bottom:11px"><div class="gold" style="width:12px;height:12px;color:#fff;font-size:8px;font-weight:700;text-align:center;line-height:12px">2.</div><div><div class="h" style="color:var(--gold-2)">Lorem ipsum</div><div class="txt w">Lorem ipsum dolor sit amet, consectetuer adipiscing elit, sed diam nonummy nibh euismod tincid</div></div></div>
    <div style="display:flex;gap:4px"><div class="gold" style="width:12px;height:12px;color:#fff;font-size:8px;font-weight:700;text-align:center;line-height:12px">3.</div><div><div class="h" style="color:var(--gold-2)">Lorem ipsum</div><div class="txt w">Lorem ipsum dolor sit amet, consectetuer adipiscing elit, sed diam nonummy nibh euismod tincid</div></div></div>
  </div>
  <svg class="abs" style="left:128px;top:40px" width="215" height="150" viewBox="0 0 215 150" font-family="Montserrat,sans-serif" font-size="4" fill="#555">
    <line x1="0" y1="110" x2="210" y2="110" stroke="#ccc" stroke-width=".5"/>
    <g><rect x="14" y="34" width="5" height="76" fill="#231f20"/><rect x="21" y="68" width="5" height="42" fill="#a97c35"/><rect x="28" y="75" width="5" height="35" fill="#e2c98a"/>
    <text x="13" y="31">43%</text><text x="20" y="65">24%</text><text x="27" y="72">20%</text><text x="20" y="120">1</text></g>
    <g><rect x="66" y="32" width="5" height="78" fill="#231f20"/><rect x="73" y="66" width="5" height="44" fill="#a97c35"/><rect x="80" y="75" width="5" height="35" fill="#e2c98a"/>
    <text x="65" y="29">44%</text><text x="60" y="63">25%</text><text x="79" y="72">20%</text><text x="72" y="120">2</text></g>
    <g><rect x="118" y="48" width="5" height="62" fill="#231f20"/><rect x="125" y="57" width="5" height="53" fill="#a97c35"/><rect x="132" y="78" width="5" height="32" fill="#e2c98a"/>
    <text x="114" y="45">35%</text><text x="124" y="54">30%</text><text x="124" y="76">18%</text><text x="124" y="120">3</text></g>
    <g><rect x="170" y="30" width="5" height="80" fill="#231f20"/><rect x="177" y="61" width="5" height="49" fill="#a97c35"/><rect x="184" y="22" width="5" height="88" fill="#e2c98a"/>
    <text x="166" y="27">45%</text><text x="175" y="58">28%</text><text x="182" y="19">50%</text><text x="176" y="120">4</text></g>
    <g font-size="3.5"><rect x="60" y="127" width="3" height="3" fill="#231f20"/><text x="64" y="130">Series1</text><rect x="84" y="127" width="3" height="3" fill="#a97c35"/><text x="88" y="130">Series2</text><rect x="108" y="127" width="3" height="3" fill="#e2c98a"/><text x="112" y="130">Series3</text></g>
  </svg>
  <div class="num">7</div>
</section>

<!-- 11 education -->
<section class="slide">
  <div class="gold-v abs" style="left:0;top:0;width:5px;height:198px"></div>
  <div class="title" style="left:18px;top:10px">Our Education</div>
  <div class="dash" style="left:18px;top:25px"></div>
  <div class="abs" style="left:52px;top:38px;width:260px;height:110px;background:#f3f3f3;border-radius:30px" role="img" aria-label="Faint world map backdrop"></div>
  <svg class="abs" style="left:60px;top:46px" width="240" height="100" viewBox="0 0 240 100" font-family="Montserrat,sans-serif">
    <g fill="none" stroke="#231f20" stroke-width="1.6">
      <rect x="10" y="2" width="58" height="86" rx="6"/>
      <rect x="92" y="2" width="58" height="86" rx="6"/>
      <rect x="174" y="2" width="58" height="86" rx="6"/>
      <path d="M68 80 L92 10"/><path d="M150 80 L174 10"/>
    </g>
    <g fill="#a97c35"><circle cx="39" cy="20" r="4"/><rect x="117" y="16" width="8" height="6"/><path d="M198 16 L206 24 L206 18 Z"/></g>
    <g font-size="5" font-weight="700" fill="#231f20" text-anchor="middle"><text x="39" y="36">IDEA</text><text x="121" y="36">PROMOTION</text><text x="203" y="36">GROWTH</text></g>
    <g font-size="3.2" fill="#777" text-anchor="middle">
      <text x="39" y="44">Lorem ipsum dolor sit</text><text x="39" y="48">amet, consectetuer</text><text x="39" y="52">adipiscing elit, sed</text><text x="39" y="56">diam nonummy nibh</text><text x="39" y="60">euismod tincidunt</text><text x="39" y="64">ut laoreet dolore</text>
      <text x="121" y="44">Lorem ipsum dolor sit</text><text x="121" y="48">amet, consectetuer</text><text x="121" y="52">adipiscing elit, sed</text><text x="121" y="56">diam nonummy nibh</text><text x="121" y="60">euismod tincidunt</text><text x="121" y="64">ut laoreet dolore</text>
      <text x="203" y="44">Lorem ipsum dolor sit</text><text x="203" y="48">amet, consectetuer</text><text x="203" y="52">adipiscing elit, sed</text><text x="203" y="56">diam nonummy nibh</text><text x="203" y="60">euismod tincidunt</text><text x="203" y="64">ut laoreet dolore</text>
    </g>
  </svg>
  <div class="txt abs" style="left:45px;top:150px;width:265px;text-align:center">Lorem ipsum dolor sit amet, consectetuer adipiscing elit, sed diam nonummy nibh euismod tincidunt ut laoreet dolore magna aliquam erat volutpat. Ut wisi enim ad minim veniam, quis nostrud exerci tation ullamcorper suscipit lobortis nisl ut aliquip ex ea commodo consequat. Duis autem vel eum iriure dolor in hendrerit</div>
  <div class="num">8</div>
</section>

<!-- 12 cycle -->
<section class="slide">
  <div class="gold-v abs" style="right:0;top:0;width:5px;height:198px"></div>
  <div class="title" style="left:18px;top:14px">Text<br>Added Hare</div>
  <div class="dash" style="left:18px;top:45px"></div>
  <div class="txt abs" style="left:18px;top:54px;width:105px">Lorem ipsum dolor sit amet, consectetuer adipiscing elit, sed diam nonummy nibh.<br><br>Ut wisi enim ad minim veniam, quis nostrud exerci tation ullamcorper suscipit lobortis. Ut wisi enim ad minim veniam, quis nostrud exerci tation ullamcorper suscipit</div>
  <div class="gold abs" style="left:0;top:114px;width:113px;height:60px"></div>
  <div class="abs" style="left:16px;top:120px;width:92px"><div class="h w">● &nbsp;Lorem ipsum</div><div class="txt w" style="margin:1px 0 8px 8px">Lorem ipsum dolor sit amet, consectetuer adipiscing elit, sed diam nonummy nibh euismod</div><div class="h w">● &nbsp;Lorem ipsum</div><div class="txt w" style="margin:1px 0 0 8px">Lorem ipsum dolor sit amet, consectetuer adipiscing elit, sed diam nonummy nibh euismod</div></div>
  <svg class="abs" style="left:150px;top:30px" width="200" height="160" viewBox="0 0 200 160" font-family="Montserrat,sans-serif">
    <path d="M110 20 A62 62 0 1 1 55 35" fill="none" stroke="#231f20" stroke-width="4"/>
    <path d="M40 58 L30 72" stroke="#231f20" stroke-width="3"/><path d="M24 62 L30 74 L40 66" fill="none" stroke="#231f20" stroke-width="2.5"/>
    <g fill="#c9a45a"><circle cx="130" cy="30" r="17"/><circle cx="145" cy="95" r="13"/><circle cx="117" cy="138" r="11"/><circle cx="77" cy="137" r="9"/></g>
    <g fill="#fff"><circle cx="130" cy="30" r="11"/><circle cx="145" cy="95" r="8"/><circle cx="117" cy="138" r="6"/><circle cx="77" cy="137" r="5"/></g>
    <g fill="#a97c35"><circle cx="130" cy="30" r="5"/><circle cx="145" cy="95" r="4"/><circle cx="117" cy="138" r="3"/><circle cx="77" cy="137" r="2.5"/></g>
    <g fill="#a97c35"><rect x="70" y="62" width="3" height="8"/><rect x="75" y="58" width="3" height="12"/><rect x="80" y="64" width="3" height="6"/></g>
    <text x="77" y="80" font-size="4.5" font-weight="700" text-anchor="middle" fill="#231f20">MAIN TITLE</text>
    <g font-size="3" fill="#777" text-anchor="middle"><text x="77" y="85">Lorem ipsum dolor sit</text><text x="77" y="89">amet, consectetuer</text></g>
    <g font-size="3.6" font-weight="700" fill="#231f20"><text x="150" y="22">80%</text><text x="120" y="68">80%</text><text x="95" y="108">50%</text><text x="130" y="152">75%</text></g>
    <g font-size="4.2" font-weight="700" fill="#231f20"><text x="162" y="35">Your Title</text><text x="172" y="74">Your Title</text><text x="155" y="124">Your Title</text><text x="4" y="110">Your Title</text></g>
  </svg>
  <div class="num">9</div>
</section>

<!-- 13 service -->
<section class="slide">
  <div class="gold abs" style="left:0;top:0;width:63px;height:24px"></div>
  <div class="photo" style="left:22px;top:21px;width:132px;height:155px" role="img" aria-label="Businessman and businesswoman reviewing a tablet"></div>
  <div class="gold abs" style="left:50px;top:155px;width:76px;height:21px;color:#fff;font-size:10px;font-weight:700;text-align:center;line-height:21px">Service</div>
  <div class="gold-v abs" style="right:0;top:0;width:5px;height:198px"></div>
  <div class="icon" style="left:174px;top:36px;width:22px;height:22px"></div>
  <div class="item" style="left:208px;top:36px;width:130px"><div class="h">Project name</div><div class="txt">Lorem ipsum dolor sit amet, nec an dictas equidem appellantur, ut has commune accommodare. Mea illum, ludus solet idpro.</div></div>
  <div class="icon" style="left:174px;top:87px;width:22px;height:22px"></div>
  <div class="item" style="left:208px;top:87px;width:130px"><div class="h">Project name</div><div class="txt">Lorem ipsum dolor sit amet, nec an dictas equidem appellantur, ut has commune accommodare. Mea illum, ludus solet idpro.</div></div>
  <div class="icon" style="left:174px;top:138px;width:22px;height:22px"></div>
  <div class="item" style="left:208px;top:138px;width:130px"><div class="h">Project name</div><div class="txt">Lorem ipsum dolor sit amet, nec an dictas equidem appellantur, ut has commune accommodare. Mea illum, ludus solet idpro.</div></div>
  <div class="num">10</div>
</section>

<!-- 14 swot -->
<section class="slide">
  <div class="gold-v abs" style="right:0;top:0;width:5px;height:198px"></div>
  <div class="title" style="left:14px;top:10px">Text Added Hare</div>
  <div class="dash" style="left:14px;top:25px"></div>
  <svg class="abs" style="left:70px;top:40px" width="220" height="150" viewBox="0 0 220 150" font-family="Montserrat,sans-serif">
    <line x1="106" y1="0" x2="106" y2="150" stroke="#bbb" stroke-width=".5" stroke-dasharray="2 1"/>
    <line x1="20" y1="75" x2="190" y2="75" stroke="#bbb" stroke-width=".5" stroke-dasharray="2 1"/>
    <circle cx="84" cy="53" r="23" fill="#9c6f2c"/><circle cx="128" cy="53" r="23" fill="#d6b56e"/>
    <circle cx="84" cy="97" r="23" fill="#d9b978"/><circle cx="128" cy="97" r="23" fill="#a57432"/>
    <circle cx="106" cy="75" r="16" fill="#231f20"/>
    <text x="106" y="77" font-size="4.2" font-style="italic" font-weight="700" fill="#fff" text-anchor="middle">ANALYSIS</text>
    <g font-size="17" font-weight="600" fill="#fff" text-anchor="middle"><text x="80" y="58">S</text><text x="133" y="58">W</text><text x="80" y="104">O</text><text x="133" y="104">T</text></g>
    <g font-size="4" font-style="italic" font-weight="700" fill="#231f20"><text x="14" y="6">STRENGTHS</text><text x="152" y="4">WEAKNESSES</text><text x="6" y="110">OPPORTUNITIES</text><text x="160" y="106">THREATS</text></g>
    <g font-size="2.8" fill="#777"><text x="16" y="12">· Good location</text><text x="16" y="17">· Very affordable prices</text><text x="16" y="22">· Variety of activities</text><text x="16" y="27">· Personal trainer</text>
    <text x="154" y="10">· Not many promotions</text><text x="154" y="15">  during the year</text><text x="154" y="21">· Small fitness</text><text x="154" y="26">  training rooms</text><text x="154" y="32">· Presence in social</text><text x="154" y="37">  networks can</text><text x="154" y="42">  be improved</text>
    <text x="8" y="116">· Hiring more graphic</text><text x="8" y="121">  designers and</text><text x="8" y="126">  marketing members</text><text x="8" y="133">· An app can be practical</text><text x="8" y="138">  to track results, find</text><text x="8" y="143">  information about</text>
    <text x="162" y="112">· Others gyms have more</text><text x="162" y="117">  space to workout and</text><text x="162" y="122">  training clubs</text><text x="162" y="129">· There are many free</text><text x="162" y="134">  fitness apps</text><text x="162" y="141">· Pricier competitors</text><text x="162" y="146">  have nutritionist</text></g>
  </svg>
  <div class="num">11</div>
</section>

<!-- 15 four cards -->
<section class="slide">
  <div class="title" style="left:18px;top:11px">Text Added Hare</div>
  <div class="dash" style="left:18px;top:27px"></div>
  <div class="abs" style="left:50px;top:40px;width:270px;height:105px;background:#f4f4f4;border-radius:30px" role="img" aria-label="Faint world map backdrop"></div>
  <div class="card" style="left:53px;top:58px;width:56px;height:74px;padding:12px 3px 3px"><div class="h">Lorem ipsum</div><div class="txt">ipsum dolor sit amet, cons ectetuer adipiscing elit, sed diam nonummy nibh euismod tincidunt ut laoreet dolore magna aliquam erat volutpat.</div></div>
  <div class="card" style="left:120px;top:58px;width:56px;height:74px;border-color:var(--gold-2);padding:12px 3px 3px"><div class="h g">Lorem ipsum</div><div class="txt">ipsum dolor sit amet, cons ectetuer adipiscing elit, sed diam nonummy nibh euismod tincidunt ut laoreet dolore magna aliquam erat volutpat.</div></div>
  <div class="card" style="left:187px;top:58px;width:56px;height:74px;padding:12px 3px 3px"><div class="h">Lorem ipsum</div><div class="txt">ipsum dolor sit amet, cons ectetuer adipiscing elit, sed diam nonummy nibh euismod tincidunt ut laoreet dolore magna aliquam erat volutpat.</div></div>
  <div class="card" style="left:254px;top:58px;width:56px;height:74px;border-color:var(--gold-2);padding:12px 3px 3px"><div class="h g">Lorem ipsum</div><div class="txt">ipsum dolor sit amet, cons ectetuer adipiscing elit, sed diam nonummy nibh euismod tincidunt ut laoreet dolore magna aliquam erat volutpat.</div></div>
  <div class="icon" style="left:71px;top:50px;width:18px;height:18px;background:var(--gold-4)"></div>
  <div class="icon" style="left:138px;top:50px;width:18px;height:18px;background:var(--ink)"></div>
  <div class="icon" style="left:205px;top:50px;width:18px;height:18px;background:var(--gold-4)"></div>
  <div class="icon" style="left:272px;top:50px;width:18px;height:18px;background:var(--ink)"></div>
  <div class="abs" style="left:54px;top:153px;font-size:10px;font-weight:700">+ 35k</div>
  <div class="txt abs" style="left:54px;top:168px;width:200px">Lorem ipsum dolor sit amet, consectetuer adipiscing elit, sed diam nonummy nibh euismod tincidunt ut laoreet dolore magna aliquam erat volutpat. Ut wisi enim ad minim veniam, quis nostrud exerci tation ullamcorper</div>
  <div class="num">12</div>
</section>

<!-- 16 diagonal -->
<section class="slide">
  <div class="title" style="left:13px;top:12px">Text Added Hare</div>
  <div class="dash" style="left:13px;top:28px"></div>
  <div class="txt abs" style="left:22px;top:42px;width:60px;font-size:4px">Lorem ipsum dolor sit amet,consec tetuer adipiscing elit, sed diam nonummy nibh euismod tincidunt erat volutpat.<br><br>Ut wisi enim ad minim veniam, quis nostrud exerci tation ullamcorper suscipit lobortis nisl ut aliquip ex ea commodo consequat.</div>
  <div class="gold abs" style="left:100px;top:30px;width:100px;height:146px;clip-path:polygon(45% 0,100% 0,55% 100%,0 100%)"></div>
  <div class="photo dark" style="left:80px;top:30px;width:112px;height:146px;clip-path:polygon(50% 0,100% 0,50% 100%,0 100%);background:linear-gradient(160deg,#2b2620,#8a6b34,#1e1c1a)" role="img" aria-label="Silhouette of a person at an office window"></div>
  <div class="icon" style="left:182px;top:48px;width:20px;height:20px;background:#fff;border:1.5px solid var(--gold-2)"></div>
  <div class="item" style="left:218px;top:50px;width:125px"><div class="h">We Before Me</div><div class="txt">ipsum dolor sit amet, cons ectetuer adipiscing elit, sed diam nonummy nibh euismod tincidunt ut laoreet</div></div>
  <div class="icon" style="left:162px;top:94px;width:20px;height:20px;background:#fff;border:1.5px solid var(--gold-2)"></div>
  <div class="item" style="left:198px;top:96px;width:130px"><div class="h">We Are Good People</div><div class="txt">ipsum dolor sit amet, cons ectetuer adipiscing elit, sed diam nonummy nibh euismod tincidunt laoreet dolore magna aliquam erat volutpat.</div></div>
  <div class="icon" style="left:140px;top:140px;width:20px;height:20px;background:#fff;border:1.5px solid var(--gold-2)"></div>
  <div class="item" style="left:176px;top:143px;width:130px"><div class="h">We Work with Heart</div><div class="txt">ipsum dolor sit amet, cons ectetuer adipiscing elit, sed diam nonummy nibh euismod tincidunt</div></div>
  <div class="num">13</div>
</section>

<!-- 17 donuts -->
<section class="slide">
  <div class="gold-v abs" style="right:0;top:0;width:5px;height:198px"></div>
  <div class="title" style="left:0;width:352px;top:14px;text-align:center">Text Added Hare</div>
  <div class="txt abs" style="left:64px;top:30px;width:224px;text-align:center">Lorem ipsum dolor sit amet, consectetuer adipiscing elit, sed diam nonummy nibh euismod tincidunt ut laoreet dolore magna aliquam erat volutpat. Ut wisi enim ad minim veniam, quis nostrud exerci tation ullamcorper suscipit lobortis nisl ut aliquip ex ea commodo consequat. Duis autem vel eum iriure</div>
  <svg class="abs" style="left:40px;top:75px" width="280" height="100" viewBox="0 0 280 100" font-family="Montserrat,sans-serif">
    <g fill="none" stroke-width="4" transform="rotate(-90)">
      <circle cx="-40" cy="45" r="27" stroke="#eee"/><circle cx="-40" cy="45" r="27" stroke="#231f20" stroke-dasharray="85 170"/>
      <circle cx="-40" cy="139" r="27" stroke="#eee"/><circle cx="-40" cy="139" r="27" stroke="#a97c35" stroke-dasharray="127 170"/>
      <circle cx="-40" cy="233" r="27" stroke="#eee"/><circle cx="-40" cy="233" r="27" stroke="#d6b56e" stroke-dasharray="68 170"/>
    </g>
    <g font-size="14" font-weight="600" fill="#231f20" text-anchor="middle"><text x="45" y="45">50%</text><text x="139" y="45">75%</text><text x="233" y="45">40%</text></g>
    <g font-size="3.2" fill="#777" text-anchor="middle"><text x="45" y="82">Lorem ipsum dolor sit amet amet</text><text x="45" y="86">consectetur dolor</text><text x="139" y="82">Lorem ipsum dolor sit amet amet</text><text x="139" y="86">consectetur dolor</text><text x="233" y="82">Lorem ipsum dolor sit amet amet</text><text x="233" y="86">consectetur dolor</text></g>
  </svg>
  <div class="num">14</div>
</section>

<!-- 18 list + dark box -->
<section class="slide">
  <div class="title" style="left:13px;top:10px">Text Added Hare</div>
  <div class="dash" style="left:13px;top:26px"></div>
  <div class="item" style="left:38px;top:46px;width:130px"><div class="h">01. Aliquam Erat Volutpat</div><div class="txt" style="margin-left:9px">Lorem ipsum dolor sit amet, consectetuer adipiscing elit, sed diam nonummy nibh euismod tincidunt ut laoreet.</div></div>
  <div class="item" style="left:38px;top:77px;width:130px"><div class="h">02. Consectetuer Adipiscing Elit</div><div class="txt" style="margin-left:9px">Lorem ipsum dolor sit amet, consectetuer adipiscing elit, sed diam nonummy nibh euismod tincidunt ut laoreet</div></div>
  <div class="item" style="left:38px;top:108px;width:130px"><div class="h">03. Duis Autem Vel Eum</div><div class="txt" style="margin-left:9px">Lorem ipsum dolor sit amet, consectetuer adipiscing elit, sed diam nonummy nibh euismod tincidunt.</div></div>
  <div class="item" style="left:38px;top:139px;width:130px"><div class="h">04. Aliquam Erat Volutpat</div><div class="txt" style="margin-left:9px">Lorem ipsum dolor sit amet, consectetuer adipiscing elit, sed diam nonummy nibh euismod tincidunt ut laoreet.</div></div>
  <div class="dark-bg abs" style="left:190px;top:42px;width:121px;height:122px"></div>
  <div class="icon" style="left:176px;top:58px;width:22px;height:22px;border:2px solid #fff"></div>
  <div class="item" style="left:212px;top:55px;width:90px"><div class="h w">Lorem Ipsum</div><div class="txt w">Ipsum dolor sit amet, cons ectetuer adipiscing elit, sed diam nonummy nibh euismod tincidunt ut laoreet</div></div>
  <div class="icon" style="left:176px;top:94px;width:22px;height:22px;border:2px solid #fff"></div>
  <div class="item" style="left:212px;top:92px;width:90px"><div class="h w">Lorem Ipsum</div><div class="txt w">Ipsum dolor sit amet, cons ectetuer adipiscing elit, sed diam nonummy nibh euismod tincidunt ut laoreet</div></div>
  <div class="icon" style="left:176px;top:130px;width:22px;height:22px;border:2px solid #fff"></div>
  <div class="item" style="left:212px;top:130px;width:90px"><div class="h w">Lorem Ipsum</div><div class="txt w">Ipsum dolor sit amet, cons ectetuer adipiscing elit, sed diam nonummy nibh euismod tincidunt</div></div>
  <div class="num">15</div>
</section>

<!-- 19 options -->
<section class="slide">
  <div class="title" style="left:13px;top:13px">Text Added Hare</div>
  <div class="dash" style="left:13px;top:29px"></div>
  <svg class="abs" style="left:22px;top:86px" width="40" height="42" viewBox="0 0 40 42"><path d="M0 0 H18 L38 21 L18 42 H0 L20 21 Z" fill="#ececec"/></svg>
  <div class="photo" style="left:83px;top:42px;width:67px;height:78px" role="img" aria-label="Colleagues working together at a desk"></div>
  <div class="photo" style="left:168px;top:42px;width:67px;height:78px" role="img" aria-label="Team meeting around a table"></div>
  <div class="photo" style="left:254px;top:42px;width:67px;height:78px" role="img" aria-label="Businesspeople shaking hands"></div>
  <div class="item" style="left:83px;top:126px;width:67px"><div class="h"><span style="color:var(--gold-4)">First</span> Option</div><div class="txt">Lorem ipsum dolor sit consectetuer adipiscing elit, sed diam nonummy nibh euismod tincidunt ut laoreet dolore magna aliquam erat volutpat. Ut wisi enim ad minim veniam, quis nostrud</div></div>
  <div class="item" style="left:168px;top:126px;width:67px"><div class="h"><span style="color:var(--gold-4)">Second</span> Option</div><div class="txt">Lorem ipsum dolor sit consectetuer adipiscing elit, sed diam nonummy nibh euismod tincidunt ut laoreet dolore magna aliquam erat volutpat. Ut wisi enim ad minim veniam, quis nostrud</div></div>
  <div class="item" style="left:254px;top:126px;width:67px"><div class="h"><span style="color:var(--gold-4)">Third</span> Option</div><div class="txt">Lorem ipsum dolor sit consectetuer adipiscing elit, sed diam nonummy nibh euismod tincidunt ut laoreet dolore magna aliquam erat volutpat. Ut wisi enim ad minim veniam, quis nostrud</div></div>
  <div class="num">16</div>
</section>

<!-- 20 section break -->
<section class="slide">
  <div class="gold abs" style="left:16px;top:13px;width:320px;height:171px;background:linear-gradient(120deg,#7d5b22,#b88d3f 50%,#8c6a2c)" role="img" aria-label="Gold-toned office scene"></div>
  <div class="abs" style="left:177px;top:66px;color:#fff;font-size:17px;line-height:1.1">Section<br><b>Break</b></div>
  <div class="txt abs w" style="left:177px;top:108px;width:120px;font-size:4px">Lorem ipsum dolor sit amet, consectetuer sed diam nonummy nibh euismod tincid</div>
</section>

<!-- 21 hub -->
<section class="slide">
  <div class="title" style="left:13px;top:17px">Text Added Hare</div>
  <div class="dash" style="left:13px;top:33px"></div>
  <svg class="abs" style="left:35px;top:50px" width="170" height="130" viewBox="0 0 170 130">
    <circle cx="46" cy="59" r="44" fill="none" stroke="#231f20" stroke-width="3"/>
    <circle cx="46" cy="59" r="36" fill="#c9a45a"/>
    <circle cx="46" cy="59" r="13" fill="none" stroke="#fff" stroke-width="1.5"/>
    <path d="M38 63 L44 56 L48 60 L55 53" fill="none" stroke="#fff" stroke-width="1.5"/>
    <g fill="none" stroke="#231f20" stroke-width=".8">
      <path d="M95 55 L110 13 H133"/><path d="M95 59 H133"/><path d="M95 63 L110 107 H133"/>
    </g>
  </svg>
  <div class="icon" style="left:180px;top:54px;width:20px;height:20px"></div>
  <div class="item" style="left:218px;top:48px;width:125px"><div class="h">Project name</div><div class="txt">Lorem ipsum dolor sit amet, nec an dictas equidem appellantur, ut has commune accommodare. Mea illum, ludus solet idpro.</div></div>
  <div class="icon" style="left:180px;top:100px;width:20px;height:20px"></div>
  <div class="item" style="left:218px;top:94px;width:125px"><div class="h">Project name</div><div class="txt">Lorem ipsum dolor sit amet, nec an dictas equidem appellantur, ut has commune accommodare. Mea illum, ludus solet idpro.</div></div>
  <div class="icon" style="left:180px;top:147px;width:20px;height:20px"></div>
  <div class="item" style="left:218px;top:141px;width:125px"><div class="h">Project name</div><div class="txt">Lorem ipsum dolor sit amet, nec an dictas equidem appellantur, ut has commune accommodare. Mea illum, ludus solet idpro.</div></div>
  <div class="num">18</div>
</section>

<!-- 22 six blocks -->
<section class="slide">
  <div class="gold abs" style="left:140px;top:0;width:212px;height:10px"></div>
  <div class="title" style="left:13px;top:10px">Text Added Hare</div>
  <div class="dash" style="left:13px;top:26px"></div>
  <div class="item" style="left:26px;top:49px;width:95px"><div class="h g" style="font-size:4.5px">1. Text Added Here</div><div class="txt">Lorem ipsum dolor sit amet, cons ectetuer adipiscing elit, sed diam nonummy nibh euismod tincidunt ut laoreet dolore magna aliquam erat volutpat. Ut wisi enim ad minim veniam.<br><br>Lorem ipsum dolor sit amet, consectetuer adipiscing elit, sed diam nonummy nibh euismod</div></div>
  <div class="item" style="left:131px;top:49px;width:95px"><div class="h g" style="font-size:4.5px">1. Text Added Here</div><div class="txt">Lorem ipsum dolor sit amet, cons ectetuer adipiscing elit, sed diam nonummy nibh euismod tincidunt ut laoreet dolore magna aliquam erat volutpat. Ut wisi enim ad minim veniam.<br><br>Lorem ipsum dolor sit amet, consectetuer adipiscing elit, sed diam nonummy nibh euismod</div></div>
  <div class="item" style="left:234px;top:49px;width:95px"><div class="h g" style="font-size:4.5px">1. Text Added Here</div><div class="txt">Lorem ipsum dolor sit amet, cons ectetuer adipiscing elit, sed diam nonummy nibh euismod tincidunt ut laoreet dolore magna aliquam erat volutpat. Ut wisi enim ad minim veniam.<br><br>Lorem ipsum dolor sit amet, consectetuer adipiscing elit, sed diam nonummy nibh euismod</div></div>
  <div class="item" style="left:26px;top:113px;width:95px"><div class="h g" style="font-size:4.5px">1. Text Added Here</div><div class="txt">Lorem ipsum dolor sit amet, cons ectetuer adipiscing elit, sed diam nonummy nibh euismod tincidunt ut laoreet dolore magna aliquam erat volutpat. Ut wisi enim ad minim veniam.<br><br>Lorem ipsum dolor sit amet, consectetuer adipiscing elit, sed diam nonummy nibh euismod</div></div>
  <div class="item" style="left:131px;top:113px;width:95px"><div class="h g" style="font-size:4.5px">1. Text Added Here</div><div class="txt">Lorem ipsum dolor sit amet, cons ectetuer adipiscing elit, sed diam nonummy nibh euismod tincidunt ut laoreet dolore magna aliquam erat volutpat. Ut wisi enim ad minim veniam.<br><br>Lorem ipsum dolor sit amet, consectetuer adipiscing elit, sed diam nonummy nibh euismod</div></div>
  <div class="item" style="left:234px;top:113px;width:95px"><div class="h g" style="font-size:4.5px">1. Text Added Here</div><div class="txt">Lorem ipsum dolor sit amet, cons ectetuer adipiscing elit, sed diam nonummy nibh euismod tincidunt ut laoreet dolore magna aliquam erat volutpat. Ut wisi enim ad minim veniam.<br><br>Lorem ipsum dolor sit amet, consectetuer adipiscing elit, sed diam nonummy nibh euismod</div></div>
  <div class="num">19</div>
</section>

<!-- 23 quadrant circle -->
<section class="slide">
  <div class="title" style="left:13px;top:10px">Text Added Hare</div>
  <div class="dash" style="left:13px;top:26px"></div>
  <svg class="abs" style="left:126px;top:54px" width="100" height="100" viewBox="0 0 100 100" font-family="Montserrat,sans-serif">
    <path d="M50 50 L50 2 A48 48 0 0 1 98 50 Z" fill="#c9a45a"/>
    <path d="M50 50 L98 50 A48 48 0 0 1 50 98 Z" fill="#231f20"/>
    <path d="M50 50 L50 98 A48 48 0 0 1 2 50 Z" fill="#d6b56e"/>
    <path d="M50 50 L2 50 A48 48 0 0 1 50 2 Z" fill="#231f20"/>
    <g stroke="#fff" stroke-width="2"><line x1="50" y1="0" x2="50" y2="100"/><line x1="0" y1="50" x2="100" y2="50"/></g>
    <g fill="#fff"><circle cx="24" cy="24" r="4"/><circle cx="76" cy="24" r="4"/><circle cx="24" cy="76" r="4"/><circle cx="76" cy="76" r="4"/></g>
    <circle cx="50" cy="50" r="22" fill="#fff"/>
    <text x="50" y="48" font-size="7.5" font-weight="600" text-anchor="middle" fill="#231f20">Text</text>
    <text x="50" y="57" font-size="7.5" font-weight="600" text-anchor="middle" fill="#231f20">Added</text>
  </svg>
  <div class="item" style="left:38px;top:55px;width:80px;text-align:right"><div class="h">Text Here</div><div class="txt">Lorem ipsum dolor sit amet, consectetuer adipiscing elit, sed dammy nibh euismod tincidunt ut laoreet dolore</div></div>
  <div class="item" style="left:38px;top:123px;width:80px;text-align:right"><div class="h">Text Here</div><div class="txt">Lorem ipsum dolor sit amet, consectetuer adipiscing elit, sed dammy nibh euismod tincidunt ut laoreet dolore</div></div>
  <div class="item" style="left:234px;top:55px;width:80px"><div class="h">Text Here</div><div class="txt">Lorem ipsum dolor sit amet, consectetuer adipiscing elit, sed dammy nibh euismod tincidunt ut laoreet dolore</div></div>
  <div class="item" style="left:234px;top:123px;width:80px"><div class="h">Text Here</div><div class="txt">Lorem ipsum dolor sit amet, consectetuer adipiscing elit, sed dammy nibh euismod tincidunt ut laoreet dolore</div></div>
  <div class="num">20</div>
</section>

<!-- 24 steps -->
<section class="slide">
  <div class="title" style="left:13px;top:10px">Text Added Hare</div>
  <div class="dash" style="left:13px;top:26px"></div>
  <svg class="abs" style="left:32px;top:70px" width="300" height="24" viewBox="0 0 300 24" font-family="Montserrat,sans-serif">
    <defs><linearGradient id="stepGold" x1="0" x2="1"><stop offset="0" stop-color="#8c6a2c"/><stop offset=".5" stop-color="#f1dfa4"/><stop offset="1" stop-color="#a97c35"/></linearGradient></defs>
    <polygon points="0,0 52,0 62,11 52,22 0,22 10,11" fill="url(#stepGold)"/>
    <polygon points="55,0 107,0 117,11 107,22 55,22 65,11" fill="#231f20"/>
    <polygon points="110,0 162,0 172,11 162,22 110,22 120,11" fill="url(#stepGold)"/>
    <polygon points="165,0 217,0 227,11 217,22 165,22 175,11" fill="#231f20"/>
    <polygon points="220,0 272,0 282,11 272,22 220,22 230,11" fill="url(#stepGold)"/>
    <g font-size="6" font-weight="600" fill="#fff" text-anchor="middle"><text x="33" y="13">STEP 01</text><text x="88" y="13">STEP 02</text><text x="143" y="13">STEP 03</text><text x="198" y="13">STEP 04</text><text x="253" y="13">STEP 05</text></g>
  </svg>
  <div class="item" style="left:35px;top:110px;width:54px;text-align:center"><div class="h">Project name</div><div class="txt">Lorem Ipsum is simply dummy unknown printer took a galley of type and scrambled it to make.</div></div>
  <div class="item" style="left:90px;top:110px;width:54px;text-align:center"><div class="h">Project name</div><div class="txt">Lorem Ipsum is simply dummy unknown printer took a galley of type and scrambled it to make.</div></div>
  <div class="item" style="left:145px;top:110px;width:54px;text-align:center"><div class="h">Project name</div><div class="txt">Lorem Ipsum is simply dummy unknown printer took a galley of type and scrambled it to make.</div></div>
  <div class="item" style="left:200px;top:110px;width:54px;text-align:center"><div class="h">Project name</div><div class="txt">Lorem Ipsum is simply dummy unknown printer took a galley of type and scrambled it to make.</div></div>
  <div class="item" style="left:255px;top:110px;width:54px;text-align:center"><div class="h">Project name</div><div class="txt">Lorem Ipsum is simply dummy unknown printer took a galley of type and scrambled it to make.</div></div>
  <div class="num">21</div>
</section>

<!-- 25 timeline -->
<section class="slide">
  <div class="gold abs" style="left:0;top:14px;width:183px;height:19px;color:#fff;font-size:11px;font-weight:700;padding:3px 0 0 17px">Project Timeline - 2024</div>
  <svg class="abs" style="left:30px;top:55px" width="300" height="110" viewBox="0 0 300 110" font-family="Montserrat,sans-serif">
    <defs><linearGradient id="barGold" x1="0" x2="1"><stop offset="0" stop-color="#8c6a2c"/><stop offset=".5" stop-color="#f1dfa4"/><stop offset="1" stop-color="#a97c35"/></linearGradient></defs>
    <polygon points="6,52 60,52 56,60 0,60" fill="#231f20"/>
    <polygon points="62,52 116,52 112,60 56,60" fill="url(#barGold)"/>
    <polygon points="118,52 172,52 168,60 112,60" fill="#231f20"/>
    <polygon points="174,52 228,52 224,60 168,60" fill="url(#barGold)"/>
    <polygon points="230,52 284,52 292,60 224,60" fill="#231f20"/>
    <g font-size="4.2" font-weight="600" fill="#fff" text-anchor="middle"><text x="31" y="58">1990</text><text x="86" y="58">2001</text><text x="142" y="58">2007</text><text x="198" y="58">2012</text><text x="256" y="58">2020</text></g>
    <g stroke="#231f20" stroke-width="1.2"><line x1="31" y1="36" x2="31" y2="48"/><line x1="142" y1="36" x2="142" y2="48"/><line x1="256" y1="36" x2="256" y2="48"/></g>
    <g stroke="#a97c35" stroke-width="1.2"><line x1="86" y1="64" x2="86" y2="76"/><line x1="198" y1="64" x2="198" y2="76"/></g>
    <g font-size="5" font-weight="700" fill="#231f20" text-anchor="middle"><text x="31" y="12">Your Title</text><text x="142" y="12">Your Title</text><text x="256" y="12">Your Title</text><text x="86" y="86">Your Title</text><text x="198" y="86">Your Title</text></g>
    <g font-size="3.6" fill="#555" text-anchor="middle"><text x="31" y="18">Refers to a good or</text><text x="31" y="23">service being offered</text><text x="142" y="18">Refers to a good or</text><text x="142" y="23">service being offered</text><text x="256" y="18">Refers to a good or</text><text x="256" y="23">service being offered</text><text x="86" y="92">Refers to a good or</text><text x="86" y="97">service being offered</text><text x="198" y="92">Refers to a good or</text><text x="198" y="97">service being offered</text></g>
  </svg>
  <div class="num">22</div>
</section>

<!-- 26 dark panel list -->
<section class="slide">
  <div class="photo dark" style="left:0;top:0;width:123px;height:198px" role="img" aria-label="Dark monochrome office backdrop"></div>
  <div class="abs" style="top:30px;transform:rotate(90deg);transform-origin:left top;color:#fff;font-size:11px;font-weight:700;letter-spacing:2.5px;white-space:nowrap;left:46px">TEXT ADDED</div>
  <div class="gold abs" style="left:68px;top:33px;width:126px;height:34px;box-shadow:3px 3px 4px rgba(0,0,0,.35);color:var(--ink);font-size:10px;font-weight:700;padding:10px 0 0 16px">1. Lorem Ipsum</div>
  <div class="gold abs" style="left:68px;top:83px;width:126px;height:34px;box-shadow:3px 3px 4px rgba(0,0,0,.35);color:var(--ink);font-size:10px;font-weight:700;padding:10px 0 0 16px">2. Lorem Ipsum</div>
  <div class="gold abs" style="left:68px;top:142px;width:126px;height:34px;box-shadow:3px 3px 4px rgba(0,0,0,.35);color:var(--ink);font-size:10px;font-weight:700;padding:10px 0 0 16px">3. Lorem Ipsum</div>
  <div class="title" style="left:216px;top:56px;font-size:10px">Text<br>Added Hare</div>
  <div class="dash" style="left:216px;top:85px"></div>
  <div class="txt abs" style="left:216px;top:94px;width:115px">Lorem ipsum dolor sit amet, consectetuer adipiscing elit, sed diam nonummy nibh .<br><br>Ut wisi enim ad minim veniam, quis nostrud exerci tation ullamcorper suscipit lobortis. Ut wisi enim ad minim veniam, quis nostrud exerci tation ullamcorper suscipit</div>
  <div class="num">23</div>
</section>

<!-- 27 icon timeline -->
<section class="slide">
  <div class="title" style="left:15px;top:13px">Text Added Hare</div>
  <div class="dash" style="left:15px;top:29px"></div>
  <svg class="abs" style="left:20px;top:60px" width="320" height="60" viewBox="0 0 320 60" font-family="Montserrat,sans-serif">
    <defs><linearGradient id="lineGold" x1="0" x2="1"><stop offset="0" stop-color="#8c6a2c"/><stop offset=".5" stop-color="#e2c98a"/><stop offset="1" stop-color="#a97c35"/></linearGradient></defs>
    <rect x="4" y="40" width="300" height="4" fill="url(#lineGold)"/>
    <polygon points="304,36 314,42 304,48" fill="#a97c35"/>
    <g fill="none" stroke-width="4"><circle cx="56" cy="18" r="16" stroke="#a97c35"/><circle cx="118" cy="18" r="16" stroke="#a97c35"/><circle cx="180" cy="18" r="16" stroke="#a97c35"/><circle cx="242" cy="18" r="16" stroke="#d6b56e"/></g>
    <g fill="none" stroke="#231f20" stroke-width="1.2"><circle cx="56" cy="18" r="6"/><path d="M56 14 V18 H59"/><circle cx="118" cy="19" r="5"/><ellipse cx="180" cy="15" rx="6" ry="2"/><path d="M174 15 V22 A6 2 0 0 0 186 22 V15"/><circle cx="241" cy="17" r="4"/><path d="M244 20 L248 24"/></g>
    <g font-size="3.8" font-weight="600" fill="#fff" text-anchor="middle"><text x="56" y="43.5">Step 01</text><text x="118" y="43.5">Step 02</text><text x="180" y="43.5">Step 03</text><text x="242" y="43.5">Step 04</text></g>
    <g stroke="#555" stroke-width=".6"><line x1="56" y1="45" x2="56" y2="56"/><line x1="118" y1="45" x2="118" y2="56"/><line x1="180" y1="45" x2="180" y2="56"/><line x1="242" y1="45" x2="242" y2="56"/></g>
  </svg>
  <div class="item" style="left:50px;top:119px;width:52px;text-align:center"><div class="h">Lorem Ipsum</div><div class="txt">Lorem ipsum dolor sit amet, consectetuer adipiscing elit, sed diam nonummy nibh euismod tincidunt ut laoreet dolore magna aliquam erat</div></div>
  <div class="item" style="left:112px;top:119px;width:52px;text-align:center"><div class="h">Lorem Ipsum</div><div class="txt">Lorem ipsum dolor sit amet, consectetuer adipiscing elit, sed diam nonummy nibh euismod tincidunt ut laoreet dolore magna aliquam erat</div></div>
  <div class="item" style="left:174px;top:119px;width:52px;text-align:center"><div class="h">Lorem Ipsum</div><div class="txt">Lorem ipsum dolor sit amet, consectetuer adipiscing elit, sed diam nonummy nibh euismod tincidunt ut laoreet dolore magna aliquam erat</div></div>
  <div class="item" style="left:236px;top:119px;width:52px;text-align:center"><div class="h">Lorem Ipsum</div><div class="txt">Lorem ipsum dolor sit amet, consectetuer adipiscing elit, sed diam nonummy nibh euismod tincidunt ut laoreet dolore magna aliquam erat</div></div>
  <div class="num">24</div>
</section>

<!-- 28 phones -->
<section class="slide">
  <div class="title" style="left:22px;top:20px;font-size:17px;font-weight:800;line-height:1.1">Text<br><span style="color:var(--gold-4)">Added</span><br>Here</div>
  <div class="gold abs" style="left:0;top:100px;width:131px;height:76px"></div>
  <div class="abs" style="left:22px;top:106px;width:105px">
    <div style="display:flex;gap:4px;margin-bottom:6px"><div class="dark-bg" style="width:11px;height:11px;color:#fff;font-size:7px;font-weight:700;text-align:center;line-height:11px">1.</div><div><div class="h w">Lorem ipsum</div><div class="txt w">Lorem ipsum dolor sit amet, consectetuer adipiscing elit, sed diam nonummy nibh euismod</div></div></div>
    <div style="display:flex;gap:4px;margin-bottom:6px"><div class="dark-bg" style="width:11px;height:11px;color:#fff;font-size:7px;font-weight:700;text-align:center;line-height:11px">2.</div><div><div class="h w">Lorem ipsum</div><div class="txt w">Lorem ipsum dolor sit amet, consectetuer adipiscing elit, sed diam nonummy nibh euismod</div></div></div>
    <div style="display:flex;gap:4px"><div class="dark-bg" style="width:11px;height:11px;color:#fff;font-size:7px;font-weight:700;text-align:center;line-height:11px">3.</div><div><div class="h w">Lorem ipsum</div><div class="txt w">Lorem ipsum dolor sit amet, consectetuer adipiscing elit, sed diam nonummy nibh euismod</div></div></div>
  </div>
  <div class="abs" style="left:140px;top:40px;width:190px;height:110px;background:#f4f4f4;border-radius:30px" role="img" aria-label="Faint world map backdrop"></div>
  <div class="card" style="left:157px;top:30px;width:41px;height:90px;border-radius:5px;border-width:1.5px"><div class="h" style="font-size:4px;margin-top:6px">Lorem<br>ipsum dolor</div><div class="txt" style="margin-top:20px;font-size:2.8px">To introduce the audience to the changing landscape of marketing and share knowledge.</div></div>
  <div class="card" style="left:212px;top:53px;width:41px;height:90px;border-radius:5px;border-width:1.5px"><div class="h" style="font-size:4px;margin-top:6px">Dolor sit<br>amet, conse</div><div class="txt" style="margin-top:20px;font-size:2.8px">You will learn concepts and ideas in digital marketing and tools for success.</div></div>
  <div class="card" style="left:266px;top:83px;width:41px;height:90px;border-radius:5px;border-width:1.5px"><div class="h" style="font-size:4px;margin-top:6px">Consec</div><div class="txt" style="margin-top:24px;font-size:2.8px">You are expected to pass 80% of the evaluation test to be certified.</div></div>
  <div class="num">25</div>
</section>

<!-- 29 team -->
<section class="slide">
  <div class="gold abs" style="left:0;top:20px;width:352px;height:44px;color:#fff;font-size:15px;font-weight:700;text-align:center;padding-top:12px">The Team Members</div>
  <div class="abs" style="left:0;top:84px;width:352px;display:flex;justify-content:space-around;padding:0 30px">
    <div style="width:62px;text-align:center"><div style="width:26px;height:26px;border-radius:50%;background:var(--photo);border:2px solid #fff;box-shadow:0 0 0 1px var(--gold-2);margin:-12px auto 4px" role="img" aria-label="Team member portrait"></div><div class="h">JOHN SMITH</div><div class="txt">Lorem ipsum dolor sit amet, cons ectetuer adipiscing elit, sed diam nonummy nibh euismod.<br><br>Ut wisi enim ad minim veniam, quis nostrud</div></div>
    <div style="width:62px;text-align:center"><div style="width:26px;height:26px;border-radius:50%;background:var(--photo);border:2px solid #fff;box-shadow:0 0 0 1px var(--gold-2);margin:-12px auto 4px" role="img" aria-label="Team member portrait"></div><div class="h">MILLIE SMITH</div><div class="txt">Lorem ipsum dolor sit amet, cons ectetuer adipiscing elit, sed diam nonummy nibh euismod.<br><br>Ut wisi enim ad minim veniam, quis nostrud</div></div>
    <div style="width:62px;text-align:center"><div style="width:26px;height:26px;border-radius:50%;background:var(--photo);border:2px solid #fff;box-shadow:0 0 0 1px var(--gold-2);margin:-12px auto 4px" role="img" aria-label="Team member portrait"></div><div class="h">JOHN SMITH</div><div class="txt">Lorem ipsum dolor sit amet, cons ectetuer adipiscing elit, sed diam nonummy nibh euismod.<br><br>Ut wisi enim ad minim veniam, quis nostrud</div></div>
    <div style="width:62px;text-align:center"><div style="width:26px;height:26px;border-radius:50%;background:var(--photo);border:2px solid #fff;box-shadow:0 0 0 1px var(--gold-2);margin:-12px auto 4px" role="img" aria-label="Team member portrait"></div><div class="h">MILLIE SMITH</div><div class="txt">Lorem ipsum dolor sit amet, cons ectetuer adipiscing elit, sed diam nonummy nibh euismod.<br><br>Ut wisi enim ad minim veniam, quis nostrud</div></div>
  </div>
  <div class="num">26</div>
</section>

<!-- 30 thank you -->
<section class="slide">
  <div class="brand" style="left:196px;top:40px;font-size:8px"><i></i>Brindle Oak MSP</div>
  <div class="title" style="left:22px;top:50px;font-size:19px">Thank You</div>
  <svg class="abs" style="left:22px;top:84px" width="14" height="70" viewBox="0 0 14 70" fill="#a97c35">
    <path d="M3 2 L6 1 L8 5 L6 7 Q7 10 10 11 L12 9 L14 12 L12 14 Q4 13 1 5 Z"/>
    <path d="M1 30 L13 25 L8 37 L7 32 Z"/>
    <path d="M7 52 L1 58 H3 V64 H6 V60 H8 V64 H11 V58 H13 Z"/>
  </svg>
  <div class="abs" style="left:39px;top:82px;width:1px;height:14px;background:var(--ink)"></div>
  <div class="abs" style="left:39px;top:106px;width:1px;height:14px;background:var(--ink)"></div>
  <div class="abs" style="left:39px;top:132px;width:1px;height:14px;background:var(--ink)"></div>
  <div class="txt abs" style="left:45px;top:83px;font-size:4px;color:#444">+1 555 014 2277<br>+1 555 014 2288</div>
  <div class="txt abs" style="left:45px;top:107px;font-size:4px;color:#444">www.brindleoakmsp.com<br>hello@brindleoakmsp.com</div>
  <div class="txt abs" style="left:45px;top:133px;font-size:4px;color:#444">48 Harbor Lane, Oakridge,<br>Stateland, 20418.</div>
</section>

</main>
</body>
</html>
```